Bright Path Flyer Design for Virtual Online Clinic. -5.5 x 8.5 inches (half sheet)

We need a clean, modern flyer design for Bright Path, a new virtual walk-in clinic based in British Columbia. The flyer will be used in libraries, pharmacies, and community centers to help residents easily access primary care through their Bright Path NFC access card.
The flyer will ask a question : NEED A DOCTOR? This should be large and attention grabbing.
The design should clearly feature a Bright Path card image (the access card) as the centerpiece and visually show how patients can use it to book appointments. The tone should feel trustworthy, healthcare-oriented, and community-friendly — clean fonts, clear spacing, and strong readability from a distance.

Side One: This card has the NFC Access Card.
NEED A DOCTOR? (Large Font, Attention Grabbing)
How to Book an Appointment using your Bright Path Card
Step 1: Tap Your Card on Your Phone
Hold your card near the back of your phone.
It will activate automatically — no app needed.
The Bright Path scheduler will open.
Step 2: Schedule Your Appointment
Select your clinical concern.
Choose your time window.
Register (only once).
Confirm your appointment.
Step 3: Relax, we’ll take care of the rest
A doctor will call during your scheduled time.
Once booked, you’ll be able to call our office.
No emails, no texts — just a real person.
It’s that simple.
Side Two:
About Bright Path
Created by Dr. Marcus Ferrigan
Bright Path was founded to make healthcare simple and convenient. Prescription renewals. Common infections. Medical notes. And so much more.
Our doctors can address 120+ health concerns virtually — providing quality care without the waiting room. No waiting rooms. Just real doctors providing real care.
Why Patients Choose Bright Path
Easy access – book and be seen from anywhere in BC.
Effortless booking – tap your Bright Path Card to begin.
Trusted physicians – every visit is with a licensed BC family doctor.
How It Works
Book your visit — choose a time window that fits your day.
Join the queue — you’ll be called when it’s your turn.
Speak directly with your doctor — simple, secure, and stress-free.
Convenient Care for Common Concerns

Additional Details.
Please find the domain to be launched soon. I've attached the NFC card file for review, it is 85.5 mm x 54 mm. The card will be glued to the flyer.
I've attached examples of flyers but they are not the look I am seeking and I am looking for creative solutions.
Thank you!
http://brightpath-example.test/

Adult Patients in British Columbia

Healthcare

• Looking for clean lines, uniform appearance, and high legibility i.e poppins

0054AA
0677BA
7BADD7
CADEEF
E8F1F8

• Need A Doctor?
• Elegant style, not too busy, clear layout.
• Clutter, look cheap - review examples.

```html
<!DOCTYPE html>
<html lang="en">
<head>
<meta charset="utf-8">
<title>Bright Path – Need A Doctor? Flyer</title>
<link href="https://fonts.googleapis.com/css2?family=Poppins:wght@300;400;500;600;700;800&display=swap" rel="stylesheet">
<style>
  :root {
    --navy: #27418a;
    --ink-blue: #2c4a9a;
    --photo-top: #5d6a9c;
    --photo-bottom: #7f8bb5;
    --mist: #e8f1f8;
    --mist-deep: #dfe6f1;
    --green: #3bb58a;
    --white: #ffffff;
    --ink: #141a2a;
    --muted: #3a4256;
    --stage: #e6e6e6;
  }
  * { box-sizing: border-box; margin: 0; padding: 0; }
  html, body { width: 1200px; height: 892px; overflow: hidden; }
  body {
    background: var(--stage);
    font-family: "Poppins", sans-serif;
    position: relative;
  }
  .flyer {
    position: absolute;
    left: 325px; top: 21px;
    width: 550px; height: 850px;
    overflow: hidden;
    background: linear-gradient(180deg, var(--mist) 0%, var(--mist-deep) 100%);
    box-shadow: 0 14px 40px rgba(0,0,0,.18);
  }
  .hero-photo {
    position: absolute; left: 0; top: 0;
    width: 100%; height: 390px;
    background: linear-gradient(160deg, var(--photo-top) 0%, var(--photo-bottom) 70%, #9aa3c6 100%);
  }
  .brand-mark {
    position: absolute; top: 52px; left: 0; width: 100%;
    text-align: center;
    color: var(--white); font-weight: 400; font-size: 22px; letter-spacing: .5px;
  }
  .headline {
    position: absolute; top: 92px; left: 0; width: 100%;
    text-align: center; color: var(--white);
    font-weight: 500; font-size: 62px; line-height: 1; letter-spacing: 1px;
  }

  .access-card {
    position: absolute; left: 103px; top: 220px;
    width: 344px; height: 217px;
    border-radius: 22px; overflow: hidden;
    background: var(--white);
    box-shadow: 0 10px 24px rgba(20,30,70,.25);
  }
  .access-card .card-panel { position: absolute; left: 0; top: 0; width: 130px; height: 100%; }
  .access-card .card-name {
    position: absolute; left: 140px; top: 78px;
    font-size: 34px; font-weight: 400; color: var(--ink-blue);
  }
  .access-card .card-tap {
    position: absolute; left: 196px; bottom: 30px;
    font-size: 11px; color: var(--ink-blue);
  }
  .access-card .card-wave { position: absolute; right: 22px; bottom: 26px; width: 32px; height: 20px; }

  .booking-title {
    position: absolute; top: 470px; left: 0; width: 100%;
    text-align: center; color: var(--ink);
    font-size: 21px; font-weight: 400; line-height: 1.3;
  }
  .booking-title strong { font-weight: 700; }

  .footer-band { position: absolute; left: 0; bottom: 0; width: 100%; height: 310px; }

  .steps {
    position: absolute; top: 600px; left: 22px; right: 22px;
    display: flex; gap: 12px;
  }
  .step {
    position: relative; flex: 1;
    background: var(--white); border-radius: 20px;
    padding: 40px 10px 16px; min-height: 132px;
    text-align: center;
    box-shadow: 0 6px 16px rgba(20,30,70,.18);
  }
  .step-icon {
    position: absolute; top: -48px; left: 50%; transform: translateX(-50%);
    width: 64px; height: 64px; border-radius: 50%;
    background: var(--white); border: 1.5px solid var(--ink-blue);
    display: flex; align-items: center; justify-content: center;
  }
  .step-icon svg { width: 36px; height: 36px; }
  .step-badge {
    position: absolute; top: 10px; left: 50%; transform: translateX(-50%);
    background: var(--green); color: var(--white);
    font-size: 9px; font-weight: 600; padding: 2px 10px; border-radius: 10px;
  }
  .step h3 { font-size: 12px; font-weight: 700; line-height: 1.2; color: var(--ink); margin: 6px 0 6px; }
  .step p { font-size: 7.5px; line-height: 1.35; color: var(--muted); }

  .cta {
    position: absolute; top: 758px; left: 0; width: 100%; text-align: center;
  }
  .cta-main { color: var(--white); font-weight: 700; font-size: 26px; letter-spacing: .5px; }
  .cta-sub { color: var(--green); font-weight: 400; font-size: 13px; letter-spacing: .5px; margin-top: -2px; }
  .fine-print {
    position: absolute; bottom: 16px; left: 0; width: 100%; text-align: center;
    color: var(--white); font-size: 7.5px; letter-spacing: 2px;
  }
</style>
</head>
<body>
  <main class="flyer">
    <div class="hero-photo" role="img" aria-label="Blue-tinted photo of a doctor at a desk with a stethoscope, writing notes beside a patient"></div>

    <div class="brand-mark">Bright Path</div>
    <h1 class="headline">Need A Doctor?</h1>

    <div class="access-card">
      <svg class="card-panel" viewBox="0 0 130 217" preserveAspectRatio="none" role="img" aria-label="Blue card panel with a faint decorative pattern">
        <path d="M0 0 H95 C70 60 120 120 90 170 C80 190 95 205 100 217 H0 Z" fill="var(--ink-blue)"/>
      </svg>
      <div class="card-name">Bright Path</div>
      <div class="card-tap">Tap Here to Book</div>
      <svg class="card-wave" viewBox="0 0 32 20" aria-hidden="true" fill="none" stroke="var(--ink-blue)" stroke-width="1.5">
        <rect x="1" y="4" width="14" height="12" rx="2"/>
        <path d="M19 6 Q22 10 19 14"/><path d="M23 4 Q27 10 23 16"/><path d="M27 2 Q32 10 27 18"/>
      </svg>
    </div>

    <h2 class="booking-title">How to <strong>Book an Appointment</strong> using your<br>Bright Path Card</h2>

    <svg class="footer-band" viewBox="0 0 550 310" preserveAspectRatio="none" aria-hidden="true">
      <path d="M0 310 V120 C80 60 140 70 200 95 C300 135 420 60 550 20 V310 Z" fill="var(--navy)"/>
    </svg>

    <section class="steps">
      <article class="step">
        <div class="step-icon">
          <svg viewBox="0 0 36 36" fill="none" stroke="var(--ink-blue)" stroke-width="1.6">
            <rect x="6" y="4" width="14" height="26" rx="3"/>
            <rect x="15" y="12" width="17" height="11" rx="2" fill="var(--white)"/>
            <line x1="11" y1="27" x2="15" y2="27"/>
          </svg>
        </div>
        <span class="step-badge">Step 1</span>
        <h3>Tap your card<br>on your phone</h3>
        <p>Hold your card near the back of your phone. It will activate automatically — no app needed. The Bright Path scheduler will open.</p>
      </article>
      <article class="step">
        <div class="step-icon">
          <svg viewBox="0 0 36 36" fill="none" stroke="var(--ink-blue)" stroke-width="1.6">
            <rect x="5" y="7" width="26" height="24" rx="3"/>
            <line x1="5" y1="13" x2="31" y2="13"/>
            <line x1="11" y1="4" x2="11" y2="9"/><line x1="25" y1="4" x2="25" y2="9"/>
            <circle cx="18" cy="22" r="6"/>
            <line x1="18" y1="19" x2="18" y2="25"/><line x1="15" y1="22" x2="21" y2="22"/>
          </svg>
        </div>
        <span class="step-badge">Step 2</span>
        <h3>Schedule your<br>appointment</h3>
        <p>Select your clinical concern. Choose your time window. Register (only once). Confirm your appointment.</p>
      </article>
      <article class="step">
        <div class="step-icon">
          <svg viewBox="0 0 36 36" fill="none" stroke="var(--ink-blue)" stroke-width="1.6">
            <rect x="8" y="5" width="14" height="26" rx="3"/>
            <line x1="13" y1="27" x2="17" y2="27"/>
            <path d="M25 12 Q28 16 25 20"/><path d="M28 9 Q33 16 28 23"/>
          </svg>
        </div>
        <span class="step-badge">Step 3</span>
        <h3>Relax — we'll take<br>care of the rest</h3>
        <p>A doctor will call during your scheduled time. Once booked, you'll be able to call our office. No emails, no texts — just a real person. It's that simple.</p>
      </article>
    </section>

    <div class="cta">
      <div class="cta-main">TAP YOUR CARD TO BEGIN</div>
      <div class="cta-sub">(DOMAIN LAUNCHING SOON)</div>
    </div>
    <p class="fine-print">AVAILABLE TO RESIDENTS OF BRITISH COLUMBIA. FOR URGENT EMERGENCIES CALL 911.</p>
  </main>
</body>
</html>
```